Willow Bloom Services Business Card Design

I require a business card design for my business Willow Bloom Services. The purpose of this business is to enable people to make positive change in their lives. This business offers life coaching, hypnotherapy and facilitation services. The slogan is 'Rise from the ashes and live the life you want.' Coaching services will be available internationally whilst the hypnotherapy and facilitation services will focus on delivery in south east Queensland.

The business card should be crisp, clean, professional and give the client positive feelings of achieving success.

The logo must be representative of a phoenix rising from the ashes which is a symbol of regeneration and new life. My preference is a black Phoenix on a white background similar to the Phoenix image attached to this brief. I'm happy to see other concepts you have too. The logo and business name must be scalable so it can be printed on a large outdoor sign. Therefore the following files must be provided as a minimum:
-Business card
-Logo on it's own
-Business name on it's own

The following detail must appear on either the front/back of the business card
-Logo
-Willow Bloom Services
-Rise from the ashes and live the life you want.
-Personal and business success through
-Coaching | Hypnotherapy | Facilitation
-Della Harcourt
-Founder

-Life Coach
-Clinical Hypnotherapist
-MBA (Project Management specialisation)
-Neuro Linguistic Programming Practitioner

-0418 372 906
-E: willowbloom.au@mailhaven.com
-www.willow-bloom.com.au
-Contact us now for your free 20min assessment

Please feel free to ask me as many questions as you like :) Thank you.

Hi all,  friendly reminder that the logo needs to be your own design and cannot be a Imagequarry or other purchased or free image.  

Thanks heaps
Keep the great designs coming in. You're all so talented.
Della

• Feedback from older people is that black backgrounds with lighter fonts are difficult to read so please no black backgrounds.

```html
<!DOCTYPE html>
<html lang="en">
<head>
<meta charset="utf-8">
<title>Willow Bloom Services – Business Card</title>
<link href="https://fonts.googleapis.com/css2?family=Lato:ital,wght@0,400;0,700;0,900;1,400&family=Cabin:wght@400;500&family=Oswald:wght@400&family=Lobster&family=Crimson+Pro:wght@500&display=swap" rel="stylesheet">
<style>
  :root {
    --page: #e9e6e1;
    --card: #d4a862;
    --card-light: #dbb46f;
    --crimson: #8e0f10;
    --ink: #1c1a17;
    --flame: #e6561c;
    --cta: #d4143a;
  }
  * { box-sizing: border-box; margin: 0; padding: 0; }
  html, body { width: 1200px; height: 1200px; overflow: hidden; }
  body { background: var(--page); position: relative; font-family: "Lato", sans-serif; color: var(--ink); }

  .card {
    position: absolute; width: 821px; height: 468px;
    background: radial-gradient(ellipse at 60% 40%, var(--card-light), var(--card));
    box-shadow: 0 6px 18px rgba(0,0,0,.25); overflow: hidden;
  }
  .card--front { left: 190px; top: 100px; }
  .card--back  { left: 190px; top: 630px; }

  .logo-mark { position: absolute; display: flex; align-items: center; gap: 10px; }
  .logo-mark__dot { border-radius: 50%; background: var(--crimson); flex: none; }
  .logo-mark__name { font-family: "Lato", sans-serif; font-weight: 900; color: var(--crimson); line-height: 1; }

  .front__logo { left: 40px; top: 150px; }
  .front__logo .logo-mark__dot { width: 64px; height: 64px; }
  .front__logo .logo-mark__name { font-size: 26px; }

  .offer { position: absolute; left: 365px; top: 90px; font-family: "Cabin", sans-serif; font-size: 25px; }
  .offer__list { list-style: none; margin-top: 4px; }
  .offer__list li { display: flex; align-items: center; gap: 12px; line-height: 32px; }
  .offer__icon { width: 12px; height: 18px; }

  .business-name {
    position: absolute; font-weight: 900; color: var(--crimson);
    letter-spacing: -0.5px; transform: scaleX(.9); transform-origin: left;
  }
  .front__name { left: 182px; top: 262px; font-size: 44px; }

  .rule { position: absolute; right: 0; background: var(--crimson); }
  .rule--thin-a { left: 155px; top: 318px; height: 3px; }
  .rule--thin-b { left: 155px; top: 330px; height: 3px; }
  .rule--band  { left: 175px; top: 342px; height: 18px; }

  .tagline {
    position: absolute; left: 186px; top: 370px;
    font-family: "Lobster", cursive; font-size: 23px; color: var(--flame); letter-spacing: .3px;
  }

  .back__logo { left: 28px; top: 60px; }
  .back__logo .logo-mark__dot { width: 34px; height: 34px; }
  .back__logo .logo-mark__name { font-size: 15px; width: 70px; }

  .back__name { left: 138px; top: 30px; font-size: 38px; }
  .back__rule { position: absolute; left: 132px; right: 0; top: 90px; height: 6px; background: var(--crimson); }

  .person { position: absolute; left: 305px; top: 110px; text-align: center; }
  .person__name { font-weight: 700; font-size: 27px; padding: 0 2px 2px; border-bottom: 3px solid var(--crimson); }
  .person__role { font-style: italic; font-size: 25px; margin-top: 2px; }

  .credentials { position: absolute; left: 265px; top: 195px; list-style: none;
    font-family: "Oswald", sans-serif; font-size: 21px; text-transform: uppercase; line-height: 30px; }
  .credentials li { display: flex; gap: 14px; }
  .credentials svg { width: 20px; height: 20px; margin-top: 5px; flex: none; }
  .credentials li + li { margin-top: 4px; }

  .contact { position: absolute; left: 125px; top: 340px; list-style: none; font-size: 23px; line-height: 34px; }
  .contact li { display: flex; align-items: center; gap: 14px; }
  .contact svg { width: 20px; height: 20px; flex: none; }

  .cta { position: absolute; left: 540px; top: 310px; width: 260px; text-align: center;
    font-family: "Crimson Pro", serif; font-weight: 500; font-size: 25px; line-height: 30px;
    color: var(--cta); text-transform: uppercase; letter-spacing: .5px; }
</style>
</head>
<body>

<section class="card card--front" aria-label="Card front">
  <div class="logo-mark front__logo">
    <span class="logo-mark__dot"></span>
    <span class="logo-mark__name">Willow Bloom</span>
  </div>

  <div class="offer">
    <p>Personal and Business Success through</p>
    <ul class="offer__list">
      <li><svg class="offer__icon" viewBox="0 0 12 18"><circle cx="6" cy="3" r="3" fill="#1c1a17"/><path d="M1 18 L6 6 L11 18Z" fill="#1c1a17"/></svg>Coaching</li>
      <li><svg class="offer__icon" viewBox="0 0 12 18"><circle cx="6" cy="3" r="3" fill="#1c1a17"/><path d="M1 18 L6 6 L11 18Z" fill="#1c1a17"/></svg>Hypnotherapy</li>
      <li><svg class="offer__icon" viewBox="0 0 12 18"><circle cx="6" cy="3" r="3" fill="#1c1a17"/><path d="M1 18 L6 6 L11 18Z" fill="#1c1a17"/></svg>Facilitation</li>
    </ul>
  </div>

  <h1 class="business-name front__name">WILLOW BLOOM SERVICES</h1>
  <div class="rule rule--thin-a"></div>
  <div class="rule rule--thin-b"></div>
  <div class="rule rule--band"></div>
  <p class="tagline">Rise From The Ashes And Live The Life You Want</p>
</section>

<section class="card card--back" aria-label="Card back">
  <div class="logo-mark back__logo">
    <span class="logo-mark__dot"></span>
    <span class="logo-mark__name">Willow Bloom</span>
  </div>

  <h2 class="business-name back__name">WILLOW BLOOM SERVICES</h2>
  <div class="back__rule"></div>

  <div class="person">
    <p class="person__name">Della Harcourt MBA</p>
    <p class="person__role">Founder</p>
  </div>

  <ul class="credentials">
    <li><svg viewBox="0 0 20 20"><path d="M10 1l2.6 6 6.4.6-4.9 4.2 1.5 6.3L10 14.8 4.4 18.1l1.5-6.3L1 7.6l6.4-.6z" fill="#1c1a17"/></svg>Certified Clinical Hypnotherapist</li>
    <li><svg viewBox="0 0 20 20"><path d="M10 1l2.6 6 6.4.6-4.9 4.2 1.5 6.3L10 14.8 4.4 18.1l1.5-6.3L1 7.6l6.4-.6z" fill="#1c1a17"/></svg><span>Certified Neuro Linguistic<br>Programming Practitioner</span></li>
    <li><svg viewBox="0 0 20 20"><path d="M10 1l2.6 6 6.4.6-4.9 4.2 1.5 6.3L10 14.8 4.4 18.1l1.5-6.3L1 7.6l6.4-.6z" fill="#1c1a17"/></svg>Certified Life Coach</li>
  </ul>

  <ul class="contact">
    <li><svg viewBox="0 0 20 20"><circle cx="10" cy="10" r="10" fill="#1c1a17"/><path d="M5 8c0-2 10-2 10 0v1h-3V8H8v1H5zM6 10h8l1 4H5z" fill="#d4a862"/></svg>0418.372.906</li>
    <li><svg viewBox="0 0 20 20"><rect x="1" y="4" width="18" height="12" fill="#1c1a17"/><path d="M2 5l8 6 8-6" stroke="#d4a862" stroke-width="1.5" fill="none"/></svg>willowbloom.au@mailhaven.com</li>
    <li><svg viewBox="0 0 20 20"><circle cx="10" cy="10" r="9" fill="#1c1a17"/><path d="M1 10h18M10 1v18M4 5h12M4 15h12" stroke="#d4a862" stroke-width="1.2" fill="none"/><ellipse cx="10" cy="10" rx="4" ry="9" stroke="#d4a862" stroke-width="1.2" fill="none"/></svg>www.willow-bloom.com.au</li>
  </ul>

  <p class="cta">Contact us now<br>for your free<br>20min assessment</p>
</section>

</body>
</html>
```